Billboard design for a small town Oral Surgeon

We are getting several billboards and need a design that highlights the doctors photo, and bullet points of what he does. Our business name is extremely long, so it’s a challenge to figure out how to do this. Maybe just use our logo? Open to ideas.
The logo can be shortened as designer sees fit, meaning we can drop the tag line. Important info to include:
Doctors name is Lorvik Tamsen
The highlighted bullet points are:
•Implants
•wisdom teeth
•Jaw Surgery
•facial trauma
The goal of this billboard is to let our community know that they have an option here in Ada, our town. Many still drive to the city a couple hours away not knowing they now have an option here at home. Having a hard time finding examples of what I have in mind, so hoping this will get us going. I want it as “non-busy” as possible, so no unnecessary lines or anything that competes with the information we are trying to get across.

Target Market(s)

Everyone in town, just trying to spread the word that we are here

Industry/Entity Type

Medical/surgical (oral surgery)

Font styles to use
Sans Serif

Colors
0094D4
00A9DD
6FCCEA
C7EBF8
E9F6FB

Requirements
Must have
• *New note** Due to location of billboard, I prefer the photo of doctor to be on the left side. Must look neat and professional. Must highlight what we do.
Nice to have
• Our colors are a blue-green with silver, against black or white, but I’m flexible on this, I don’t necessarily need the colors highlighted. I’m also flexible on font style, just needs to be easy to read.
Should not have
• Distracting graphics, should not look like a dental office. That’s an issue we have is people thinking we are another dental office, we do not do any general dentistry, it’s surgery only.

```html
<!DOCTYPE html>
<html lang="en">
<head>
<meta charset="utf-8">
<title>Oral Surgery Billboard</title>
<link rel="stylesheet" href="https://fonts.googleapis.com/css2?family=League+Spartan:wght@700;800&family=Montserrat:wght@600;800&display=swap">
<style>
  :root {
    --stage: #bdbdbd;
    --paper: #ffffff;
    --teal: #0a8ea8;
    --cyan: #16bde6;
    --deep: #0c3541;
    --ink: #0b3a48;
    --silver: #5d6266;
  }
  html, body {
    margin: 0;
    width: 1003px;
    height: 1200px;
    overflow: hidden;
    background: var(--stage);
  }
  .billboard {
    position: absolute;
    left: 31px;
    top: 444px;
    width: 940px;
    height: 312px;
    box-shadow: 0 10px 22px rgba(0,0,0,0.35);
  }
  .billboard svg { display: block; width: 940px; height: 312px; }
  .paper { fill: var(--paper); }
  .band { fill: var(--teal); }
  .footer-bar { fill: var(--deep); }
  .name-tag { fill: var(--cyan); }
  .pill-light { fill: var(--cyan); }
  .pill-dark { fill: var(--deep); }
  .brand-dot { fill: var(--teal); }
  .tagline {
    font-family: "Montserrat", sans-serif;
    font-weight: 800;
    font-size: 25px;
    fill: var(--paper);
  }
  .headline {
    font-family: "League Spartan", sans-serif;
    font-weight: 800;
    fill: var(--ink);
  }
  .pill-text {
    font-family: "Montserrat", sans-serif;
    font-weight: 800;
    font-size: 12px;
    text-anchor: middle;
  }
  .pill-text.on-light { fill: var(--deep); }
  .pill-text.on-dark { fill: var(--paper); }
  .brand-name {
    font-family: "Montserrat", sans-serif;
    font-weight: 600;
    font-size: 12px;
    fill: var(--silver);
    text-anchor: middle;
  }
  .phone {
    font-family: "League Spartan", sans-serif;
    font-weight: 700;
    font-size: 50px;
    fill: var(--paper);
  }
  .address {
    font-family: "Montserrat", sans-serif;
    font-weight: 800;
    font-size: 13px;
    fill: var(--paper);
  }
  .doctor-name {
    font-family: "League Spartan", sans-serif;
    font-weight: 800;
    font-size: 19px;
    fill: var(--deep);
  }
  .icon { fill: var(--cyan); }
</style>
</head>
<body>
  <div class="billboard">
    <svg viewBox="0 0 940 312" xmlns="http://www.w3.org/2000/svg">
      <defs>
        <linearGradient id="portrait-tone" x1="0" y1="0" x2="0" y2="1">
          <stop offset="0" stop-color="#f4f6f8"/>
          <stop offset="0.45" stop-color="#d9b8a2"/>
          <stop offset="0.7" stop-color="#1a2436"/>
          <stop offset="1" stop-color="#141c2c"/>
        </linearGradient>
      </defs>

      <rect class="paper" x="0" y="0" width="940" height="312"/>

      <!-- brand crescent -->
      <circle class="band" cx="834" cy="78" r="140"/>
      <circle class="paper" cx="828" cy="65" r="134"/>

      <!-- top band -->
      <path class="band" d="M169 0 H715 C692 37 686 67 662 67 H276 C250 67 243 16 169 0 Z"/>

      <!-- brand -->
      <g class="brand">
        <circle class="brand-dot" cx="836" cy="66" r="13"/>
        <text class="brand-name" x="834" y="112">PRAIRIE RIDGE ORAL</text>
        <text class="brand-name" x="834" y="127">&amp; FACIAL SURGERY</text>
      </g>

      <!-- tagline -->
      <text class="tagline" x="272" y="50" textLength="400" lengthAdjust="spacing">THE NEW LOCALE IN ADA</text>

      <!-- headline -->
      <text class="headline" x="254" y="129" font-size="60" textLength="444" lengthAdjust="spacingAndGlyphs">ORAL SURGERY</text>
      <text class="headline" x="254" y="174" font-size="41" textLength="441" lengthAdjust="spacingAndGlyphs">&amp; COSMETIC SERVICES</text>

      <!-- services -->
      <g class="services">
        <rect class="pill-light" x="254" y="191" width="106" height="24" rx="12"/>
        <text class="pill-text on-light" x="307" y="207">Implants</text>
        <rect class="pill-dark" x="365" y="191" width="106" height="24" rx="12"/>
        <text class="pill-text on-dark" x="418" y="207">Wisdom teeth</text>
        <rect class="pill-light" x="476" y="191" width="106" height="24" rx="12"/>
        <text class="pill-text on-light" x="529" y="207">Jaw Surgery</text>
        <rect class="pill-dark" x="587" y="191" width="106" height="24" rx="12"/>
        <text class="pill-text on-dark" x="640" y="207">Facial trauma</text>
      </g>

      <!-- footer -->
      <rect class="footer-bar" x="233" y="244" width="707" height="68"/>

      <g class="icon" transform="translate(252 258) scale(0.62) translate(-64 -417)">
        <path d="M70 424 c6 -4 12 -3 15 2 l7 12 c2 4 0 8 -4 10 l-5 3 c3 8 9 15 17 19 l4 -5 c3 -3 7 -4 10 -1 l11 8 c4 3 4 9 0 13 l-6 5 c-22 5 -52 -25 -55 -50 c0 -6 2 -12 6 -16 Z"/>
        <path d="M95 417 a26 26 0 0 1 24 24 h-6 a20 20 0 0 0 -18 -18 Z"/>
      </g>
      <text class="phone" x="290" y="296" textLength="318" lengthAdjust="spacingAndGlyphs">(580) 555-0147</text>

      <g transform="translate(630 258) scale(0.62) translate(-662 -417)">
        <path class="icon" d="M680 417 c-10 0 -18 8 -18 18 c0 14 18 32 18 32 s18 -18 18 -32 c0 -10 -8 -18 -18 -18 Z"/>
        <circle class="footer-bar" cx="680" cy="434" r="6"/>
      </g>
      <text class="address" x="660" y="272">412 N Cedar Hollow St. Ada,</text>
      <text class="address" x="660" y="291">OK 74820, USA</text>

      <!-- portrait -->
      <rect x="0" y="11" width="233" height="301" fill="url(#portrait-tone)" role="img" aria-label="Portrait photo of Dr. Lorvik Tamsen smiling, in a dark suit, white shirt and red tie"/>

      <!-- name tag -->
      <path class="name-tag" d="M0 234 H236 C258 234 258 267 236 267 H0 Z"/>
      <text class="doctor-name" x="12" y="258" textLength="228" lengthAdjust="spacingAndGlyphs">LORVIK TAMSEN, D.D.S.</text>
    </svg>
  </div>
</body>
</html>
```